a simple functional website for an up and coming service industry business

hi ,i also require in store promotional items like business cards, flyers, Chatterbox page t-shirts for workers and want all these to have the same look and feel.i need my website to catch the eye .the idea i have in my head is something that will sell the service ,the website is a tool to get people to inquire , book or pay for an assembly service.we assemble flatpack furniture , outdoor furniture,playgrounds etc ,basically anything that comes with instructions,our biggest customer at the moment is Norvalt who we assemble nationally.i am looking for a website to be bright modern and simple to use the current website is www.brindleyfitouts.com which is dull with to many pages . i have already had a new logo designed by sketch harbour and it is lime green and sky blue in colour, a webiste i like is jobtrek q4 although it has lots of flash and my budget probably wouldn't allow that at the moment.

Target Market(s)

customer will be visiting the website to find out about the service we provide , then hopefully making contact,either booking a job or asking for a quote, i like the idea of the phone, email icons on the home screen

Industry/Entity Type

Industry

Requirements
Must have
• a contact icon: when you click on it the page with the name ,email address ,phone number, address pops up

a phone icon : when you click on it the 1300 number pops up
Nice to have
• my current website is with plume and it is www.brindleyfitouts.com

a website i really like the design of is jobtrek q4 and Norvalt

would like some pictures of modern furniture ,bbq's ,gym equipment ,playground equiptment
Should not have
• the career page or price page my current website .i don't want it on there anymore

```html
<!DOCTYPE html>
<html lang="en">
<head>
<meta charset="utf-8">
<title>Brindley Assembly</title>
<link href="https://fonts.googleapis.com/css2?family=Montserrat:wght@300;400;500;600&family=Roboto:wght@300;400&display=swap" rel="stylesheet">
<style>
:root{
  --lime:#8dc63f;
  --lime-text:#9bcc4a;
  --sky:#2a8fd1;
  --ink:#3a3a3a;
  --soft:#8a8a8a;
  --black:#000;
  --white:#fff;
  --page:#f7f7f7;
}
*{margin:0;padding:0;box-sizing:border-box}
html,body{width:1013px;height:1200px;overflow:hidden}
body{position:relative;background:var(--page);font-family:"Montserrat",sans-serif;color:var(--ink)}
.site-header{position:absolute;left:0;top:0;width:1013px;height:125px;background:var(--black)}
.brand{position:absolute;left:97px;top:44px;display:flex;align-items:center;gap:8px;color:var(--lime);font-weight:600;font-size:17px;letter-spacing:.5px}
.brand-mark{width:22px;height:22px;background:var(--lime)}
.header-contact{position:absolute;right:109px;top:24px;display:flex;align-items:center;gap:8px}
.header-phone{color:var(--lime);font-size:15px;font-weight:500}
.quick-icon{width:22px;height:22px;border-radius:50%;background:var(--lime);display:flex;align-items:center;justify-content:center}
.main-nav{position:absolute;right:109px;top:60px;display:flex;font-size:15px;color:var(--white);letter-spacing:.6px}
.main-nav span{padding:0 16px;border-left:1px solid var(--white);line-height:16px}
.main-nav span:first-child{border-left:none}
.main-nav span:last-child{padding-right:0}
.hero{position:absolute;left:0;top:125px;width:1013px;height:349px;background:linear-gradient(90deg,#b9bcbd 0%,#d9dcdc 35%,#c2c4c3 56%,#ecebe6 62%,#e8e4d8 85%,#dfe4e8 100%)}
.hero-title{position:absolute;left:652px;top:150px;font-size:25px;font-weight:500;color:#444;letter-spacing:.3px}
.hero-arrow{position:absolute;top:185px}
.hero-arrow.prev{left:77px}
.hero-arrow.next{left:908px}
.welcome{position:absolute;left:109px;top:493px;width:792px}
.section-title{color:var(--lime-text);font-weight:300;font-size:26px;letter-spacing:.5px}
.intro{margin-top:16px;font-size:11.6px;line-height:28px;text-align:justify}
.callout{margin-top:12px;font-size:18.8px;line-height:30px;font-weight:400}
.callout strong{color:var(--sky);font-weight:500}
.column{position:absolute;top:758px}
.testimonials{left:109px;width:456px}
.news{left:582px;width:319px}
.entry{position:absolute;left:0;width:100%}
.photo{position:absolute;left:0;top:0}
.testimonials .photo{width:118px;height:94px}
.news .photo{width:94px;height:94px}
.entry-text{position:absolute;right:0;font-size:11.5px;line-height:20px;color:var(--soft);text-align:justify;font-weight:300}
.testimonials .entry-text{left:133px;top:2px}
.news .entry-text{left:102px;top:2px}
.person{position:absolute;left:133px;top:70px;font-size:16px;color:#555}
.place{position:absolute;left:133px;top:91px;font-size:11.5px;color:var(--soft)}
.date{display:block;font-size:10.5px;color:#666;font-weight:400}
.site-footer{position:absolute;left:0;top:1128px;width:1013px;height:72px;background:var(--lime);font-family:"Roboto",sans-serif;color:var(--white)}
.footer-nav{position:absolute;left:110px;top:11px;font-size:12.5px;font-weight:400}
.footer-nav span{margin-right:6px}
.copyright{position:absolute;left:110px;top:39px;font-size:12px;font-weight:300}
.social{position:absolute;left:831px;top:22px;display:flex;gap:2px}
.social span{width:25px;height:25px;border-radius:50%}
</style>
</head>
<body>
<header class="site-header">
  <div class="brand"><span class="brand-mark"></span>BRINDLEY ASSEMBLY</div>
  <div class="header-contact">
    <span class="quick-icon" role="img" aria-label="Call us">
      <svg width="12" height="12" viewBox="0 0 24 24"><path d="M6.6 10.8a15.1 15.1 0 0 0 6.6 6.6l2.2-2.2a1 1 0 0 1 1-.25 11.4 11.4 0 0 0 3.6.57 1 1 0 0 1 1 1V20a1 1 0 0 1-1 1A17 17 0 0 1 3 4a1 1 0 0 1 1-1h3.5a1 1 0 0 1 1 1c0 1.25.2 2.45.57 3.6a1 1 0 0 1-.25 1z" fill="#000"/></svg>
    </span>
    <span class="quick-icon" role="img" aria-label="Contact details">
      <svg width="12" height="12" viewBox="0 0 24 24"><rect x="2" y="5" width="20" height="14" rx="1" fill="#000"/><polyline points="3,6 12,13 21,6" fill="none" stroke="#8dc63f" stroke-width="2"/></svg>
    </span>
    <span class="header-phone">Brindley 1300 418 259</span>
  </div>
  <nav class="main-nav"><span>HOME</span><span>SERVICES</span><span>CONTACT</span></nav>
</header>

<section class="hero" role="img" aria-label="Photo of a bright modern glass office fitout with a white sculpted wall and yellow lounge chairs">
  <svg class="hero-arrow prev" width="24" height="36" viewBox="0 0 24 36"><polyline points="20,3 5,18 20,33" fill="none" stroke="#8dc63f" stroke-width="5"/></svg>
  <div class="hero-title">FITOUT FURNITURE</div>
  <svg class="hero-arrow next" width="24" height="36" viewBox="0 0 24 36"><polyline points="4,3 19,18 4,33" fill="none" stroke="#8dc63f" stroke-width="5"/></svg>
</section>

<section class="welcome">
  <h1 class="section-title">Welcome to brindley Assembly</h1>
  <p class="intro">Brindley Assembly &amp; Installation are the ready to assemble fit out specialists. We assemble and install DIY flat pack indoor and outdoor furniture, across South East Queensland for the major retailers.We provide a reliable domestic or commercial service with professional and qualified installers.With the necessary builders licence, insurances and over 10 years experience in how to install, at Brindley Assembly &amp; Installation we make the job easy for you.</p>
  <p class="callout"><strong>CALL 1300 418 259</strong> to discuss your requirements and one of our prompt installers will contact you in a jiffy.</p>
</section>

<section class="column testimonials">
  <h2 class="section-title">Client Testimonials</h2>
  <article class="entry" style="top:65px">
    <div class="photo" role="img" aria-label="Portrait photo of a client in a suit" style="background:linear-gradient(135deg,#6b6a66,#3f3c38)"></div>
    <p class="entry-text">Sed ut perspiciatis unde omnis iste natus voluptatem accusantium laudantium, totam rem aperiam, eaque ipsa quae ab illo inventore .</p>
    <div class="person">Daniel Harlow</div>
    <div class="place">California</div>
  </article>
  <article class="entry" style="top:213px">
    <div class="photo" role="img" aria-label="Portrait photo of a client in a dark shirt" style="background:linear-gradient(135deg,#b5b3ae,#5a5753)"></div>
    <p class="entry-text">Sed ut perspiciatis unde omnis iste natus voluptatem accusantium laudantium, totam rem aperiam, eaque ipsa quae ab illo inventore .</p>
    <div class="person">Daniel Harlow</div>
    <div class="place">California</div>
  </article>
</section>

<section class="column news">
  <h2 class="section-title">Latest News</h2>
  <article class="entry" style="top:65px">
    <div class="photo" role="img" aria-label="Photo of an installer assembling a cabinet with a drill" style="background:linear-gradient(135deg,#e6e4df,#5d6470)"></div>
    <p class="entry-text">Lorem ipsum dolor sit amet, consectetur adipisicing elit, sed do eiusmod tempor incididunt ut labore et dolore magna aliqua. <span class="date">May 2013 ,23rd GST 22. 10</span></p>
  </article>
  <article class="entry" style="top:219px">
    <div class="photo" role="img" aria-label="Photo of an assembled outdoor playground" style="background:linear-gradient(135deg,#5f8a3c,#c8b04a 60%,#7aa24a)"></div>
    <p class="entry-text">Lorem ipsum dolor sit amet, consectetur adipisicing elit, sed do eiusmod tempor incididunt ut labore et dolore magna aliqua. <span class="date">May 2013 ,23rd GST 22. 10</span></p>
  </article>
</section>

<footer class="site-footer">
  <div class="footer-nav"><span>Home |</span> <span>Services &nbsp;|</span> <span>Contact</span></div>
  <div class="copyright">Copyright ©2013 Company Name &nbsp;- All rights reserved</div>
  <div class="social"><span style="background:#3b5b98"></span><span style="background:#2aa3df"></span><span style="background:#f07b2a"></span></div>
</footer>
</body>
</html>
```